I need a header for the web site www.harlowspipeworks.example/demo
It must include the following
Existig Logo (I will upload the .png)
Text: Serving Calgary and Surrounding Areas for Over 30 Years!
24 Hour Service
Call 403.718.2946 (Note this isn't the actual phone number I will need to be able to change the Phone number once the site is ready to put in a tracking number so I am hoping I get a PSD file with this where the text is editable)
We wnat the feel to be warm and geared more towards a residential customer rather than an industial customer.
We would like blue tones but are open to anything warm.

Size: Aprroximately 960x300

• Rounded Corners to match the content area on the site

```html
<!DOCTYPE html>
<html lang="en">
<head>
<meta charset="utf-8">
<title>Harlow's Pipeworks – Header</title>
<link rel="stylesheet" href="https://fonts.googleapis.com/css2?family=Oswald:wght@500;700&family=Roboto:wght@400;500&display=swap">
<style>
  :root {
    --tile-dark: #2c3d45;
    --tile-mid: #4b6068;
    --floor-light: #d9dbd6;
    --wall-light: #8fa0a4;
    --badge-blue: #6f93ad;
    --badge-text: #12202a;
    --ribbon-gold: #f2b51d;
    --ribbon-gold-light: #fde27a;
    --ribbon-gold-dark: #b77d07;
    --headline-yellow: #ffe41a;
    --headline-edge: #2b2a1c;
    --phone-red: #8a1218;
    --phone-panel: rgba(255, 255, 255, 0.82);
    --icon-dark: #161616;
    --brand-slate: #4a5a66;
  }

  * { box-sizing: border-box; margin: 0; padding: 0; }

  html, body {
    width: 1200px;
    height: 375px;
    overflow: hidden;
    background: #ffffff;
  }

  .site-header {
    position: relative;
    width: 1200px;
    height: 375px;
    overflow: hidden;
    font-family: "Roboto", Arial, sans-serif;
  }

  .bathroom-scene {
    position: absolute;
    inset: 0;
    background:
      linear-gradient(180deg, rgba(0,0,0,0) 55%, rgba(217,219,214,0.85) 78%, var(--floor-light) 100%),
      linear-gradient(100deg, var(--tile-mid) 0%, var(--tile-dark) 35%, var(--wall-light) 62%, var(--tile-dark) 85%, var(--tile-mid) 100%);
  }

  .brand-name {
    position: absolute;
    left: 128px;
    top: 272px;
    font-family: "Oswald", Arial, sans-serif;
    font-weight: 500;
    font-size: 24px;
    letter-spacing: 0.5px;
    color: var(--brand-slate);
  }

  .years-badge {
    position: absolute;
    left: 15px;
    top: -18px;
    width: 212px;
    height: 212px;
  }

  .years-badge svg { display: block; width: 100%; height: 100%; }
  .years-badge rect { fill: var(--badge-blue); }

  .years-badge__text {
    position: absolute;
    inset: 0;
    display: flex;
    flex-direction: column;
    align-items: center;
    padding-top: 80px;
    color: var(--badge-text);
    text-align: center;
  }

  .years-badge__lead { font-size: 19px; font-weight: 400; letter-spacing: 0.5px; }
  .years-badge__count { font-size: 29px; font-weight: 500; margin-top: 6px; }

  .service-ribbon {
    position: absolute;
    left: 40px;
    top: 175px;
    width: 252px;
    height: 36px;
    display: flex;
    align-items: center;
    justify-content: center;
    font-size: 25px;
    font-weight: 500;
    color: #ffffff;
    text-shadow: 0 1px 2px rgba(0,0,0,0.35);
    background: linear-gradient(180deg, var(--ribbon-gold-light) 0%, var(--ribbon-gold) 45%, var(--ribbon-gold-dark) 100%);
    box-shadow: 0 2px 4px rgba(0,0,0,0.3);
  }

  .service-ribbon::before,
  .service-ribbon::after {
    content: "";
    position: absolute;
    top: 6px;
    width: 18px;
    height: 36px;
    background: var(--ribbon-gold-dark);
    z-index: -1;
  }
  .service-ribbon::before { left: -10px; clip-path: polygon(0 0, 100% 0, 100% 100%, 0 100%, 40% 50%); }
  .service-ribbon::after { right: -10px; clip-path: polygon(0 0, 100% 0, 60% 50%, 100% 100%, 0 100%); }

  .headline {
    position: absolute;
    right: 48px;
    top: 14px;
    text-align: right;
    font-family: "Oswald", Arial, sans-serif;
    font-weight: 700;
    color: var(--headline-yellow);
    text-shadow:
      -2px -2px 0 var(--headline-edge), 2px -2px 0 var(--headline-edge),
      -2px 2px 0 var(--headline-edge), 2px 2px 0 var(--headline-edge),
      4px 5px 6px rgba(0,0,0,0.6);
    line-height: 1;
  }

  .headline__city { display: block; font-size: 80px; letter-spacing: 1px; transform: scaleY(1.05); }
  .headline__areas { display: block; font-size: 64px; margin-top: 4px; letter-spacing: 0.5px; }

  .phone-bar {
    position: absolute;
    right: 0;
    top: 312px;
    width: 325px;
    height: 54px;
    display: flex;
    align-items: center;
    gap: 14px;
    padding-left: 14px;
    background: var(--phone-panel);
  }

  .phone-bar__icon { width: 30px; height: 32px; flex: none; }
  .phone-bar__icon rect { fill: var(--icon-dark); }
  .phone-bar__icon path { fill: #ffffff; }

  .phone-bar__number {
    font-family: "Oswald", Arial, sans-serif;
    font-weight: 700;
    font-size: 38px;
    letter-spacing: 1px;
    color: var(--phone-red);
  }
</style>
</head>
<body>
<header class="site-header">
  <div class="bathroom-scene" role="img" aria-label="Photo of a modern bathroom with dark slate wall tiles, a white freestanding tub, yellow towels, pedestal sink and toilet on a pale tiled floor"></div>

  <div class="brand-name">Harlow's Pipeworks</div>

  <div class="years-badge">
    <svg viewBox="-106 -106 212 212" aria-hidden="true">
      <rect x="-75" y="-75" width="150" height="150"/>
      <rect x="-75" y="-75" width="150" height="150" transform="rotate(15)"/>
      <rect x="-75" y="-75" width="150" height="150" transform="rotate(30)"/>
      <rect x="-75" y="-75" width="150" height="150" transform="rotate(45)"/>
      <rect x="-75" y="-75" width="150" height="150" transform="rotate(60)"/>
      <rect x="-75" y="-75" width="150" height="150" transform="rotate(75)"/>
    </svg>
    <div class="years-badge__text">
      <span class="years-badge__lead">FOR OVER</span>
      <span class="years-badge__count">30 YEARS!</span>
    </div>
  </div>

  <div class="service-ribbon">24 Hour Service</div>

  <h1 class="headline">
    <span class="headline__city">SERVING CALGARY</span>
    <span class="headline__areas">&amp; Surrounding Areas</span>
  </h1>

  <div class="phone-bar">
    <svg class="phone-bar__icon" viewBox="0 0 30 32" aria-hidden="true">
      <rect x="0" y="0" width="30" height="32" rx="6"/>
      <path d="M10 6c1-.6 2 0 2.4.8l1.6 3.2c.4.8.1 1.6-.6 2l-1.2.8c.6 2.4 2 4.8 3.8 6.6l1.2-.8c.7-.5 1.6-.3 2.1.4l2 3c.5.8.3 1.8-.5 2.3l-1.6 1c-1.4.9-3.2.8-4.6-.2C10.4 22 7.6 17 7.2 11.6c-.1-1.6.6-3.1 1.8-4z"/>
    </svg>
    <span class="phone-bar__number">403.718.2946</span>
  </div>
</header>
</body>
</html>
```